Bref créative
The Lanternwrights
We keep the lamps lit!
Professional
Rosalind Kettering
Partner
48 Thornapple Lane
Phoenixville, PA 19460
rosalind.k.kettering@thelanternwrights.net
www.thelanternwrights.net
logo will be attached
second set of business cards needed
Dean Oltveld
dean.oltveld@thelanternwrights.net
Your Steady Counsel
Updated logo in CMYK format

```html
<!DOCTYPE html>
<html lang="en">
<head>
<meta charset="utf-8">
<title>The Lanternwrights – Folder Set</title>
<link href="https://fonts.googleapis.com/css2?family=Roboto:wght@400;700;900&display=swap" rel="stylesheet">
<style>
  :root{
    --bg:#e9e6e1;
    --orange-1:#f9a21b;
    --orange-2:#e5461c;
    --grey-1:#7d7f82;
    --grey-2:#c3c4c6;
    --paper:#ffffff;
    --ink:#1c1c1c;
    --red:#d8231f;
    --yellow-1:#ffe14a;
    --yellow-2:#f5a80c;
    --muted:#8a8a8a;
  }
  *{box-sizing:border-box;margin:0;padding:0}
  html,body{width:1200px;height:782px;overflow:hidden}
  body{background:var(--bg);font-family:"Roboto",Arial,sans-serif;position:relative}
  .spread{position:absolute;display:flex;box-shadow:0 6px 18px rgba(0,0,0,.25)}
  .spread--orange{left:120px;top:60px}
  .spread--white{left:629px;top:60px}
  .spread--grey{left:120px;top:396px}
  .cover{width:240px;height:325px;position:relative;display:flex;flex-direction:column;align-items:center}
  .cover--orange{background:linear-gradient(160deg,var(--orange-1),var(--orange-2))}
  .cover--white{background:var(--paper)}
  .cover--grey{background:linear-gradient(160deg,var(--grey-2),var(--grey-1))}
  .cover__mark{width:76px;height:76px;border-radius:50%;background:var(--red);margin-top:72px}
  .cover__tagline{margin-top:26px;font-size:12px;font-weight:700;letter-spacing:.5px;color:#fff;text-transform:uppercase;white-space:nowrap}
  .cover--white .cover__tagline{color:var(--muted)}
  .cover__contact{position:absolute;bottom:22px;left:0;right:0;text-align:center;font-size:5.5px;line-height:1.6;color:#fff}
  .cover--white .cover__contact{color:var(--muted)}
  .panel{width:235px;height:325px;position:relative;overflow:hidden;
    background:radial-gradient(circle at 55% 70%,var(--yellow-1),var(--yellow-2) 80%)}
  .panel__swoosh{position:absolute;left:0;top:0;width:235px;height:120px}
  .panel__mark{position:absolute;left:106px;top:10px;width:24px;height:24px;border-radius:50%;background:var(--red)}
  .panel__brand{position:absolute;left:0;right:0;top:40px;text-align:center}
  .panel__name{font-size:15px;font-weight:900;color:var(--ink);text-transform:uppercase;letter-spacing:-.2px;white-space:nowrap}
  .panel__slogan{font-size:7px;font-weight:700;color:var(--red);margin-top:2px;text-transform:uppercase;white-space:nowrap}
  .panel__glow{position:absolute;left:40px;top:140px;width:170px;height:170px;border-radius:50%;
    background:radial-gradient(circle,rgba(255,255,255,.35),rgba(255,255,255,0) 70%)}
  .envelope{position:absolute;left:640px;top:440px;width:440px;height:250px;background:var(--paper);
    box-shadow:0 6px 18px rgba(0,0,0,.2);overflow:hidden}
  .envelope__flap{position:absolute;inset:0}
  .envelope__mark{position:absolute;left:60px;top:40px;width:110px;height:110px;border-radius:50%;background:#f1f1f1}
</style>
</head>
<body>

<svg width="0" height="0" style="position:absolute">
  <defs>
    <symbol id="swoosh" viewBox="0 0 235 120">
      <path d="M0 0H235V70C170 60 80 72 0 110Z" fill="#fff"/>
      <path d="M0 110C80 72 170 60 235 70V80C170 70 80 82 0 118Z" fill="#1c1c1c"/>
      <path d="M0 118C80 82 170 70 235 80V90C170 80 80 92 0 125Z" fill="#d8231f"/>
      <path d="M0 125C80 92 170 80 235 90V96C170 88 80 100 0 130Z" fill="#f6c700"/>
    </symbol>
  </defs>
</svg>

<section class="spread spread--orange">
  <div class="cover cover--orange">
    <div class="cover__mark"></div>
    <p class="cover__tagline">Your Steady Counsel</p>
    <p class="cover__contact">48 Thornapple Lane, Phoenixville, PA 19460<br>Tel: 610 555 0142<br>rosalind.k.kettering@thelanternwrights.net<br>www.thelanternwrights.net</p>
  </div>
  <div class="panel">
    <svg class="panel__swoosh"><use href="#swoosh"/></svg>
    <div class="panel__mark"></div>
    <div class="panel__brand"><p class="panel__name">The Lanternwrights</p><p class="panel__slogan">We keep the lamps lit!</p></div>
    <div class="panel__glow" role="img" aria-label="Soft glowing sphere decoration"></div>
  </div>
</section>

<section class="spread spread--white">
  <div class="cover cover--white">
    <div class="cover__mark"></div>
    <p class="cover__tagline">Your Steady Counsel</p>
    <p class="cover__contact">48 Thornapple Lane, Phoenixville, PA 19460<br>Tel: 610 555 0142<br>rosalind.k.kettering@thelanternwrights.net<br>www.thelanternwrights.net</p>
  </div>
  <div class="panel">
    <svg class="panel__swoosh"><use href="#swoosh"/></svg>
    <div class="panel__mark"></div>
    <div class="panel__brand"><p class="panel__name">The Lanternwrights</p><p class="panel__slogan">We keep the lamps lit!</p></div>
    <div class="panel__glow" role="img" aria-label="Soft glowing sphere decoration"></div>
  </div>
</section>

<section class="spread spread--grey">
  <div class="cover cover--grey">
    <div class="cover__mark"></div>
    <p class="cover__tagline">Your Steady Counsel</p>
    <p class="cover__contact">48 Thornapple Lane, Phoenixville, PA 19460<br>Tel: 610 555 0142<br>dean.oltveld@thelanternwrights.net<br>www.thelanternwrights.net</p>
  </div>
  <div class="panel">
    <svg class="panel__swoosh"><use href="#swoosh"/></svg>
    <div class="panel__mark"></div>
    <div class="panel__brand"><p class="panel__name">The Lanternwrights</p><p class="panel__slogan">We keep the lamps lit!</p></div>
    <div class="panel__glow" role="img" aria-label="Soft glowing sphere decoration"></div>
  </div>
</section>

<section class="envelope">
  <svg class="envelope__flap" viewBox="0 0 440 250" preserveAspectRatio="none">
    <path d="M0 0L220 120L440 0" fill="none" stroke="#e4e4e4" stroke-width="1.5"/>
  </svg>
  <div class="envelope__mark"></div>
</section>

</body>
</html>
```